We need a product label for our smoothie kit stand up pouches

We are a smoothie based company who produces frozen smoothie kits. We need a 4x6 label produced for our smoothie kit. The label will be placed on a black matt stand up pouch. We have attached our product logo which needs to be very present on the label. We have also attached a PDF telling you what text should appear on the bag. Our product has text in both english and french. We have also attached an image of the black matt bag. The label should also blend well with the black matt bag. So you can use shades of grey and black and white with the pop of the logo.

Target Market(s)

Single or married Generation X born between 1965-1980.
Young families with working parents.(demographics)

Young millennials aged 18 to 24 years old who are extremely health and fitness conscious who try to avoid artificial ingredients.

Students living on their own on campus or apartments (demographics)

Healthy and athletic individuals who care about what they eat and drink (lifestyle)

Individuals who enjoy making healthy smoothies at home but do not have time to shop and wash and cut fruits and vegetables at home. (behaviour)

Industry/Entity Type

It Company

Font styles to use
Sans Serif

Requirements
Must have
• Brand logo----
• VERDAPULSEX
• Product ----
• READY-TO-BLEND / PRÊT-À-MIXER
• Name of Recipe-----
• ZEPHA (this will vary as we have 8 recipes)
• Messages about product-----
• DAIRY FREE / SANS PRODUIT LAITIERS
• VEGAN / VÉGÉTALIEN
• GLUTEN FREE / SANS GLUTEN
• 100% WHOLE INGREDENTS / INGRÉDIENTS ENTIERS
• Use colours in logo so it blends nicely
Nice to have
• Want it feeling fresh and modern.
• All about feeling good about yourself drinking our all natural healthy smoothies

```html
<!DOCTYPE html>
<html lang="en">
<head>
<meta charset="utf-8">
<title>ZEPHA – Ready-to-Blend Label</title>
<link rel="stylesheet" href="https://fonts.googleapis.com/css2?family=Montserrat:wght@300;400;600&display=swap">
<style>
  :root{
    --bg:#e4e4e4;
    --label:#ffffff;
    --blue:#6991cf;
    --green:#8dc23f;
    --brand:#6aa431;
    --icon:#8a8a8a;
    --caption:#6f6f6f;
    --white:#ffffff;
  }
  *{box-sizing:border-box;margin:0;padding:0}
  html,body{width:1200px;height:850px;overflow:hidden}
  body{
    background:linear-gradient(180deg,#cfcfcf 0%,var(--bg) 60%,#f2f2f2 100%);
    font-family:"Montserrat",sans-serif;
    position:relative;
  }
  .label{
    position:absolute;left:346px;top:45px;width:508px;height:760px;
    background:var(--label);border-radius:38px;overflow:hidden;
    box-shadow:0 6px 18px rgba(0,0,0,.15);
  }
  .band{position:absolute;left:0;width:150px}
  .band--recipe{top:0;height:532px;background:var(--blue)}
  .band--product{top:532px;height:228px;background:var(--green);
    display:flex;flex-direction:column;align-items:center;justify-content:center;
    color:var(--white);font-weight:400;font-size:20px;letter-spacing:2px;text-align:center;line-height:1.3}
  .band--product .rule{width:108px;height:2px;background:var(--white);margin:14px 0}
  .recipe-name{
    position:absolute;left:75px;top:266px;
    transform:translate(-50%,-50%) rotate(-90deg);
    color:var(--white);font-weight:300;font-size:112px;letter-spacing:14px;white-space:nowrap;
  }
  .brand{
    position:absolute;left:150px;right:0;top:40px;
    display:flex;flex-direction:column;align-items:center;gap:14px;
  }
  .brand-dot{width:46px;height:46px;border-radius:50%;background:var(--green)}
  .brand-name{color:var(--brand);font-weight:600;font-size:30px;letter-spacing:-.5px}
  .photo{
    position:absolute;left:150px;right:0;top:160px;height:400px;
    background:
      linear-gradient(180deg,rgba(255,255,255,0) 60%,#fff 100%),
      linear-gradient(90deg,#b8417e 0%,#c9569a 30%,#f1b15a 50%,#f4c77a 62%,#e35e74 85%,#ef8b94 100%);
  }
  .claims{
    position:absolute;left:150px;right:0;top:590px;
    display:grid;grid-template-columns:1fr 1fr;row-gap:18px;
  }
  .claim{display:flex;flex-direction:column;align-items:center;text-align:center;
    color:var(--caption);font-size:9.5px;line-height:1.2;letter-spacing:.3px}
  .claim svg{width:30px;height:30px;margin-bottom:6px}
</style>
</head>
<body>
  <main class="label">
    <div class="band band--recipe"><span class="recipe-name">ZEPHA</span></div>
    <div class="band band--product">
      <span>READY<br>-TO-<br>BLEND</span>
      <span class="rule"></span>
      <span>PRÊT<br>-À-<br>MIXER</span>
    </div>

    <header class="brand">
      <span class="brand-dot"></span>
      <span class="brand-name">VerdaPulseX</span>
    </header>

    <div class="photo" role="img" aria-label="Photo of three glasses of berry, mango and strawberry smoothies with fresh mint leaves"></div>

    <section class="claims">
      <div class="claim">
        <svg viewBox="0 0 30 30"><circle cx="15" cy="15" r="15" fill="var(--icon)"/><path d="M9 20c0-7 5-11 12-11-1 7-5 11-12 11zM9 20l7-6" stroke="#fff" stroke-width="1.6" fill="none"/></svg>
        100% NATURAL<br>NATUREL
      </div>
      <div class="claim">
        <svg viewBox="0 0 30 30"><circle cx="15" cy="15" r="15" fill="var(--icon)"/><path d="M15 8v15M15 11l-3-2M15 11l3-2M15 15l-3-2M15 15l3-2M15 19l-3-2M15 19l3-2M8 22L22 8" stroke="#fff" stroke-width="1.6" fill="none"/></svg>
        GLUTEN FREE<br>SANS GLUTEN
      </div>
      <div class="claim">
        <svg viewBox="0 0 30 30"><circle cx="15" cy="15" r="15" fill="var(--icon)"/><path d="M9 10l6 11 6-11" stroke="#fff" stroke-width="1.8" fill="none"/></svg>
        VEGAN<br>VÉGÉTALIEN
      </div>
      <div class="claim">
        <svg viewBox="0 0 30 30"><circle cx="15" cy="15" r="15" fill="var(--icon)"/><path d="M12 7h6v3l2 3v10h-10V13l2-3zM9 22L21 8" stroke="#fff" stroke-width="1.6" fill="none"/></svg>
        DAIRY FREE<br>SANS PRODUIT LAITIERS
      </div>
    </section>
  </main>
</body>
</html>
```